a4 size poster for theatre school

I am looking for an eye catching poster for my theatre school - Bright Lantern Stage school - View our website here for the style we have already www.brightlanternstage.co.uk

Wording needs to include;

* Award Winning, Accredited, Affordable Performing Arts Classes taught by Leading Industry Experts

* Ages 4- 21 years

* All classes contain all three disciplines of Drama, Singing & Dance keeping cost low and enjoyment high

* Classes offered;
Drama
PQVR
Singing
KSBU dance
Freestyle Ballet
Freestyle Tap
Contemporary
Street
Jazz Musical Theatre

* FREE casting agency for TV and Theatre Available. Ten pupils currently performing in West End Productions, 8 pupils currently on screen in TV commercials, several pupils currently working on film & TV projects for Zorbiville, Quellmark Plus & Vista 9.

* Optional KSBU and PQVR exams

* Unparalleled performance opportunities both locally and in the West End

Our quality training is evident in our pupils success

* Now in our successful 17th Year!

* Awarded recognition from the Board for Stagecraft, Voice and Movement Studies - The industry regulator for children's performing arts training.

Target Market(s)

Parents & Children ages 4-21 years

Industry/Entity Type

Performing arts

Font styles to use
Other font styles liked:
• Arvo

Colors
EB3D1F
EC4F4E
F09395
F8D3D4
FCEDEE
6B429C
8869AF
B7A5CE
E3DAEB
F3F0F8

Requirements
Must have
• A good mix of photo's pf boys & girls. Different ethnicities. Different ages
Nice to have
• Wording very clear
Should not have
• Too many words

```html
<!DOCTYPE html>
<html lang="en">
<head>
<meta charset="utf-8">
<title>Bright Lantern Stage school – Poster</title>
<link href="https://fonts.googleapis.com/css2?family=Arvo:wght@700&family=Poppins:wght@400;500;700&display=swap" rel="stylesheet">
<style>
  :root {
    --backdrop: #f5df55;
    --paper: #f7f5f2;
    --navy: #33378f;
    --indigo: #44429b;
    --violet: #5b3f9c;
    --gold: #f4c531;
    --band: #f1c232;
    --ink: #141414;
    --white: #ffffff;
  }
  * { margin: 0; padding: 0; box-sizing: border-box; }
  html, body { width: 1135px; height: 1200px; overflow: hidden; }
  body { background: var(--backdrop); position: relative; font-family: "Poppins", sans-serif; }

  .poster {
    position: absolute; left: 151px; top: 8px;
    width: 832px; height: 1184px;
    background: var(--paper);
  }
  .sheet { position: absolute; left: 18px; top: 15px; width: 795px; height: 1154px; overflow: hidden; }

  /* Top panel */
  .hero {
    position: absolute; left: 0; top: 0; width: 795px; height: 545px;
    background: linear-gradient(160deg, var(--navy) 0%, var(--indigo) 55%, var(--violet) 100%);
  }
  .hero-photo {
    position: absolute; right: 0; top: 0; width: 470px; height: 545px;
    background: radial-gradient(ellipse at 60% 35%, rgba(150,140,190,.55) 0%, rgba(80,70,140,.35) 45%, rgba(60,60,150,0) 80%);
  }
  .headline {
    position: absolute; left: 30px; top: 40px;
    font-family: "Arvo", serif; font-weight: 700; font-size: 41px; line-height: 56px;
    color: var(--gold);
  }
  .subline {
    position: absolute; left: 30px; top: 160px;
    color: var(--white); font-size: 16px; line-height: 22px;
  }
  .section-title {
    position: absolute; left: 30px;
    font-family: "Arvo", serif; font-weight: 700; font-size: 29px; color: var(--gold);
  }
  .ages { top: 244px; }
  .offered { top: 376px; }
  .ages-note {
    position: absolute; left: 30px; top: 295px;
    color: var(--white); font-size: 15px; line-height: 21px;
  }
  .class-list { position: absolute; top: 428px; list-style: none; }
  .class-list li {
    position: relative; padding-left: 32px; height: 33px;
    color: var(--white); font-size: 19px; font-weight: 500; line-height: 26px; white-space: nowrap;
  }
  .class-list li svg { position: absolute; left: 2px; top: 5px; width: 16px; height: 16px; }
  .col-a { left: 32px; }
  .col-b { left: 273px; }
  .col-c { left: 580px; }

  .brand {
    position: absolute; left: 598px; top: 48px; width: 180px;
    display: flex; align-items: center; gap: 10px;
  }
  .brand-dot { flex: none; width: 26px; height: 26px; border-radius: 50%; background: var(--gold); }
  .brand-name {
    font-family: "Poppins", sans-serif; font-weight: 700; font-size: 19px; line-height: 24px;
    color: var(--gold);
  }

  /* Yellow band */
  .facts {
    position: absolute; left: 0; top: 545px; width: 795px; height: 128px;
    background: var(--band); list-style: none; padding: 14px 36px 0 26px;
  }
  .facts li {
    position: relative; padding-left: 26px; margin-bottom: 12px;
    font-size: 13px; line-height: 17px; color: var(--ink);
  }
  .facts li svg { position: absolute; left: 0; top: 2px; width: 15px; height: 15px; }

  /* Photo grid */
  .tile { position: absolute; overflow: hidden; }
  .tile-fill { position: absolute; inset: 0; }
  .tile-caption {
    position: absolute; left: 0; right: 0; bottom: 0;
    background: linear-gradient(180deg, rgba(80,60,160,0) 0%, rgba(80,60,160,.75) 45%, rgba(70,55,160,.95) 100%);
    color: var(--white); font-weight: 700; line-height: 25px;
  }
  .tile-lions { left: 0; top: 673px; width: 377px; height: 481px; }
  .tile-lions .tile-fill { background: linear-gradient(180deg, #d9c9cf 0%, #a27d78 45%, #7e5a5c 75%, #6a4d8a 100%); }
  .tile-lions .tile-caption { padding: 40px 16px 0 18px; height: 170px; font-size: 18.5px; }
  .rule { display: block; height: 1px; background: rgba(255,255,255,.8); margin: 14px 0 10px 0; }
  .site { display: block; color: var(--gold); font-size: 19px; font-weight: 700; line-height: 28px; white-space: nowrap; letter-spacing: -0.2px; }

  .tile-bonnets { left: 383px; top: 675px; width: 412px; height: 186px; }
  .tile-bonnets .tile-fill { background: linear-gradient(120deg, #c8c3e3 0%, #e8d7c4 40%, #b09ac8 75%, #8a6fb0 100%); }
  .tile-bonnets .tile-caption { height: 90px; padding: 28px 18px 0; font-size: 18px; }

  .tile-driver { left: 383px; top: 867px; width: 203px; height: 287px; }
  .tile-driver .tile-fill { background: linear-gradient(180deg, #efe7da 0%, #d6cbbd 50%, #8e8296 80%, #6a4ea0 100%); }
  .tile-driver .tile-caption { height: 110px; padding: 27px 10px 0; font-size: 18px; }

  .tile-stage { left: 592px; top: 867px; width: 203px; height: 287px; }
  .tile-stage .tile-fill { background: linear-gradient(180deg, #b9533a 0%, #a4432f 50%, #7a3f5e 80%, #5b3f9c 100%); }
  .tile-stage .tile-caption { height: 110px; padding: 27px 12px 0; font-size: 18px; }
</style>
</head>
<body>
<main class="poster">
  <div class="sheet">

    <section class="hero">
      <div class="hero-photo" role="img" aria-label="Photo of young performers dancing on stage in costume"></div>

      <div class="brand">
        <span class="brand-dot"></span>
        <span class="brand-name">Bright Lantern Stage school</span>
      </div>

      <h1 class="headline">Award Winning,<br>Accredited, Affordable</h1>
      <p class="subline">Performing Arts Classes taught<br>by Leading Industry Experts</p>

      <h2 class="section-title ages">Ages 4- 21 years</h2>
      <p class="ages-note">All classes contain all three disciplines of Drama,<br>Singing &amp; Dance keeping cost low and enjoyment high</p>

      <h2 class="section-title offered">Classes offered</h2>
      <ul class="class-list col-a">
        <li><svg viewBox="0 0 24 24"><path fill="#f4c531" d="M12 1.5l3.1 6.9 7.4.7-5.6 5 1.7 7.4L12 17.7l-6.6 3.8 1.7-7.4-5.6-5 7.4-.7z"/></svg>Drama</li>
        <li><svg viewBox="0 0 24 24"><path fill="#f4c531" d="M12 1.5l3.1 6.9 7.4.7-5.6 5 1.7 7.4L12 17.7l-6.6 3.8 1.7-7.4-5.6-5 7.4-.7z"/></svg>PQVR</li>
        <li><svg viewBox="0 0 24 24"><path fill="#f4c531" d="M12 1.5l3.1 6.9 7.4.7-5.6 5 1.7 7.4L12 17.7l-6.6 3.8 1.7-7.4-5.6-5 7.4-.7z"/></svg>Singing</li>
      </ul>
      <ul class="class-list col-b">
        <li><svg viewBox="0 0 24 24"><path fill="#f4c531" d="M12 1.5l3.1 6.9 7.4.7-5.6 5 1.7 7.4L12 17.7l-6.6 3.8 1.7-7.4-5.6-5 7.4-.7z"/></svg>Contemporary</li>
        <li><svg viewBox="0 0 24 24"><path fill="#f4c531" d="M12 1.5l3.1 6.9 7.4.7-5.6 5 1.7 7.4L12 17.7l-6.6 3.8 1.7-7.4-5.6-5 7.4-.7z"/></svg>Street</li>
        <li><svg viewBox="0 0 24 24"><path fill="#f4c531" d="M12 1.5l3.1 6.9 7.4.7-5.6 5 1.7 7.4L12 17.7l-6.6 3.8 1.7-7.4-5.6-5 7.4-.7z"/></svg>Jazz Musical Theatre</li>
      </ul>
      <ul class="class-list col-c">
        <li><svg viewBox="0 0 24 24"><path fill="#f4c531" d="M12 1.5l3.1 6.9 7.4.7-5.6 5 1.7 7.4L12 17.7l-6.6 3.8 1.7-7.4-5.6-5 7.4-.7z"/></svg>KSBU dance</li>
        <li><svg viewBox="0 0 24 24"><path fill="#f4c531" d="M12 1.5l3.1 6.9 7.4.7-5.6 5 1.7 7.4L12 17.7l-6.6 3.8 1.7-7.4-5.6-5 7.4-.7z"/></svg>Freestyle Ballet</li>
        <li><svg viewBox="0 0 24 24"><path fill="#f4c531" d="M12 1.5l3.1 6.9 7.4.7-5.6 5 1.7 7.4L12 17.7l-6.6 3.8 1.7-7.4-5.6-5 7.4-.7z"/></svg>Freestyle Tap</li>
      </ul>
    </section>

    <ul class="facts">
      <li><svg viewBox="0 0 24 24"><path fill="#141414" d="M12 1.5l3.1 6.9 7.4.7-5.6 5 1.7 7.4L12 17.7l-6.6 3.8 1.7-7.4-5.6-5 7.4-.7z"/></svg>FREE casting agency for TV and Theatre Available. Ten pupils currently performing in West End Productions, 8 pupils currently on screen in TV commercials, several pupils currently working on film &amp; TV projects for Zorbiville, Quellmark Plus &amp; Vista 9.</li>
      <li><svg viewBox="0 0 24 24"><path fill="#141414" d="M12 1.5l3.1 6.9 7.4.7-5.6 5 1.7 7.4L12 17.7l-6.6 3.8 1.7-7.4-5.6-5 7.4-.7z"/></svg>Awarded recognition from the Board for Stagecraft, Voice and Movement Studies - The industry regulator for children's performing arts training.</li>
    </ul>

    <figure class="tile tile-lions">
      <div class="tile-fill" role="img" aria-label="Photo of two young performers in lion costumes and face paint"></div>
      <figcaption class="tile-caption">
        Unparalleled performance opportunities both locally and in the West End
        <span class="rule"></span>
        <span class="site">www.brightlanternstage.co.uk</span>
      </figcaption>
    </figure>

    <figure class="tile tile-bonnets">
      <div class="tile-fill" role="img" aria-label="Photo of young children performing in period bonnets and caps"></div>
      <figcaption class="tile-caption">Our quality training is<br>evident in our pupils success</figcaption>
    </figure>

    <figure class="tile tile-driver">
      <div class="tile-fill" role="img" aria-label="Photo of a boy in a leather jacket steering a prop car on stage"></div>
      <figcaption class="tile-caption">Optional<br>KSBU and PQVR<br>exams</figcaption>
    </figure>

    <figure class="tile tile-stage">
      <div class="tile-fill" role="img" aria-label="Photo of a pirate-themed stage production under red lights"></div>
      <figcaption class="tile-caption">Now in<br>our successful<br>17th Year!</figcaption>
    </figure>

  </div>
</main>
</body>
</html>
```